UK Based Internet hosting Company wants a vibrant eCommerce site designed.

We have only just had our logo and brand designed by Pixel Forum which went so well that we would like to open up our website design project on here too.

The company is called 'Quay Server Lantern' and we provide a range of website hosting, dedicated server, domain name and email solutions that people will be able to purchase online in neatly packaged options from the outset.

Our logo and brand is bright turquoise, black & white (samples of branding will be attached with this project) but we would like the website to be very vibrant with good use of white space rather than a black website.

We want to appeal to end users so web designers, developers and people who would like to host their website. But we also want to appeal to resellers that would like to resell our hosting packages too.

We want a big push on social media and blogging on the site as we would like our brand to be 100% up with Chatterleaf, Murmel, workLoop, Vidplume and Zorbix+. It would be great to have this integrated into the site with share buttons and rating buttons etc.

We would like to see a homepage initially with a view to providing several page layers down to help our in-house developers hook in our back-end into this front end effectively.

Great customer experience and an easy to navigate journey to the checkout when purchasing the hosting packages is paramount !!

We like how the following sites are set-out and presented:

www.brightmarrow.uk
http://www.tallyfold.co.uk
https://www.qv7.net/web-hosting/

Target Market(s)

We have 3 target markets.

Target market 1 - end users, consumers such as Web Designers, Developers and small businesses.

Target Market 2 - Resellers, small businesses that would like to resell our services.

Target Market 3 - Medium to large businesses that would like more of a bespoke solution.

Industry/Entity Type

Internet

Requirements
Must have
• Colourful, bright, bold, easy to navigate and to purchase packages.
• Plenty of call to actions, social media, ratings.
• Video case studies and testimonials would be nice.

```html
<!DOCTYPE html>
<html lang="en">
<head>
<meta charset="utf-8">
<title>Quay Server Lantern – Web Hosting</title>
<link href="https://fonts.googleapis.com/css2?family=Raleway:wght@200;300;400;500;600;700&family=Lora:ital@1&display=swap" rel="stylesheet">
<style>
:root{
  --teal:#1fb5b8;
  --teal-dark:#139fa3;
  --teal-light:#4fd0c4;
  --ink:#1c1c1c;
  --muted:#6d6d6d;
  --line:#e4e4e4;
  --navy:#141b26;
  --navy-deep:#0f141d;
  --white:#ffffff;
  --star:#f0a01c;
}
*{box-sizing:border-box;margin:0;padding:0}
html,body{width:1200px;height:2507px;overflow:hidden}
body{position:relative;font-family:'Raleway',sans-serif;color:var(--ink);background:var(--white)}
.abs{position:absolute}

/* header */
.site-header{position:absolute;left:0;top:0;width:1200px;height:115px;background:var(--white)}
.brand{position:absolute;left:99px;top:30px;display:flex;align-items:center;gap:14px}
.brand-dot{width:54px;height:54px;border-radius:50%;background:var(--teal)}
.brand-name{font-size:25px;font-weight:500;color:var(--ink);line-height:1.1;width:170px}
.main-nav a{position:absolute;top:50px;font-size:14px;font-weight:500;color:var(--ink);text-decoration:none;text-transform:uppercase}
.main-nav a.active{color:var(--teal)}
.header-rule{position:absolute;left:816px;top:0;width:1px;height:115px;background:var(--line)}
.live-chat{position:absolute;left:857px;top:43px;width:106px;height:34px;background:var(--teal);color:var(--white);font-size:11px;font-weight:600;display:flex;align-items:center;justify-content:center}
.header-phone-rule{position:absolute;left:980px;top:42px;width:1px;height:36px;background:#cfcfcf}
.header-phone{position:absolute;left:998px;top:46px;font-size:21px;font-weight:700;color:var(--ink)}

/* hero */
.hero{position:absolute;left:0;top:115px;width:1200px;height:537px;background:radial-gradient(ellipse at 50% 45%,#3a4552 0%,#1b222b 45%,#07090c 100%)}
.hero-title{position:absolute;left:0;width:1200px;text-align:center;color:var(--white)}
.hero-title.l1{top:130px;font-size:46px;font-weight:600}
.hero-title.l2{top:190px;font-size:54px;font-weight:200}
.hero-tag{position:absolute;left:0;top:283px;width:1200px;text-align:center;color:var(--white);font-size:27px;font-weight:400;word-spacing:6px}
.domain-search{position:absolute;left:344px;top:361px;width:510px;height:75px;background:rgba(255,255,255,.28)}
.domain-input{position:absolute;left:17px;top:13px;width:232px;height:49px;background:var(--white);font-size:15px;color:#555;padding-left:20px;display:flex;align-items:center}
.domain-tld{position:absolute;left:251px;top:13px;width:90px;height:49px;background:var(--teal-light);color:var(--white);font-size:15px;font-weight:600;display:flex;align-items:center;padding-left:18px}
.domain-tld svg{position:absolute;right:12px;top:20px}
.domain-btn{position:absolute;left:343px;top:13px;width:155px;height:49px;background:var(--teal);color:var(--white);font-size:12px;font-weight:600;display:flex;align-items:center;justify-content:center}
.slider-dots{position:absolute;display:flex;gap:6px}
.slider-dots i{width:8px;height:8px;border-radius:50%;background:var(--white)}
.slider-dots i.on{background:var(--teal)}

/* services */
.service{position:absolute;top:688px;width:240px;text-align:center}
.service-icon{width:118px;height:118px;border-radius:50%;background:linear-gradient(180deg,var(--teal-light),var(--teal-dark));margin:0 auto;display:flex;align-items:center;justify-content:center}
.service h3{margin-top:18px;font-size:20px;font-weight:500}
.service p{margin-top:16px;font-size:13px;line-height:23px;color:var(--muted)}
.divider{position:absolute;left:99px;top:976px;width:1002px;height:1px;background:var(--line)}

/* video case studies */
.section-title{position:absolute;font-size:30px;font-weight:500;color:var(--ink)}
.section-title span{font-weight:300}
.case{position:absolute;top:1081px;width:316px}
.case-thumb{width:316px;height:191px;background:linear-gradient(135deg,#5f6a74,#24292f);position:relative}
.case-thumb svg{position:absolute;left:138px;top:79px}
.case h4{margin-top:20px;font-size:19px;font-weight:500}
.case p{margin-top:12px;font-size:13px;line-height:23px;color:var(--muted)}
.rating{margin-top:10px;font-size:11px;color:var(--ink);display:flex;align-items:center;gap:4px}
.stars{color:var(--star);font-size:13px;letter-spacing:1px}

/* testimonials */
.testimonials{position:absolute;left:0;top:1501px;width:1200px;height:334px;background:linear-gradient(180deg,#41c1c4 0%,#1fb1b4 60%,#149ca3 100%)}
.testimonials .section-title{color:var(--white)}
.quote-card{position:absolute;top:105px;width:319px;height:152px;background:rgba(255,255,255,.35);padding:20px 20px 0 24px}
.quote-card p{font-family:'Lora',serif;font-style:italic;font-size:11.5px;line-height:20px;color:var(--white)}
.quote-by{margin-top:12px;font-size:13px;color:var(--white);font-weight:500}
.quote-by span{margin-left:14px;letter-spacing:1px}
.avatar{position:absolute;width:80px;height:80px;border-radius:50%;border:4px solid var(--white);background:linear-gradient(160deg,#e6d2c2,#b89478)}

/* social feed */
.feed-name{position:absolute;left:0;top:1933px;width:1200px;text-align:center;font-size:15px;color:var(--muted)}
.feed-name b{color:var(--teal);font-weight:500}
.feed-text{position:absolute;left:255px;top:1958px;width:690px;text-align:center;font-size:13px;line-height:22.5px;color:var(--muted)}
.feed-text a{color:var(--teal);text-decoration:none}
.feed-actions{position:absolute;left:490px;top:2045px;display:flex;gap:12px}
.feed-actions span{font-size:9.5px;color:#9a9a9a;background:#f3f3f3;padding:3px 5px;border-radius:2px}

/* footer */
.site-footer{position:absolute;left:0;top:2127px;width:1200px;height:313px;background:var(--navy)}
.foot-col{position:absolute;top:47px}
.foot-col h5{font-size:15px;font-weight:500;color:var(--teal);margin-bottom:20px}
.foot-col li{list-style:none;font-size:12px;line-height:23px;color:#e6e6e6}
.foot-col p{font-size:12px;line-height:23px;color:#e6e6e6;width:150px}
.foot-phone{font-size:25px;font-weight:600;color:var(--white);margin-top:-2px}
.foot-phone-small{font-size:12px;color:#e6e6e6;margin-top:4px}
.socials{display:flex;gap:8px;margin-top:22px}
.socials i{display:block;width:27px;height:27px;background:var(--teal)}
.tagline{position:absolute;left:0;top:257px;width:1200px;text-align:center;font-size:24px;color:var(--teal);font-weight:400}
.copy-bar{position:absolute;left:0;top:2440px;width:1200px;height:67px;background:var(--navy-deep);display:flex;align-items:center;justify-content:center;font-size:12px;color:#d8d8d8}
</style>
</head>
<body>

<header class="site-header">
  <div class="brand"><div class="brand-dot"></div><div class="brand-name">Quay Server Lantern</div></div>
  <nav class="main-nav">
    <a class="active" style="left:381px">Home</a>
    <a style="left:459px">About</a>
    <a style="left:537px">Pricing</a>
    <a style="left:624px">Domain</a>
    <a style="left:711px">Hosting</a>
  </nav>
  <div class="header-rule"></div>
  <div class="live-chat">LIVE CHAT</div>
  <div class="header-phone-rule"></div>
  <div class="header-phone">0000-7281</div>
</header>

<section class="hero">
  <div class="abs" style="inset:0" role="img" aria-label="Photo of a dark data centre aisle lined with server racks"></div>
  <h1 class="hero-title l1">We are a Proffesional</h1>
  <div class="hero-title l2">Web Hosting Services</div>
  <div class="hero-tag">modern - fast - reliable</div>
  <form class="domain-search">
    <div class="domain-input">Your Domain Name ...</div>
    <div class="domain-tld">.com
      <svg width="12" height="8" viewBox="0 0 12 8"><path d="M1 1l5 5 5-5" fill="none" stroke="#fff" stroke-width="1.6"/></svg>
    </div>
    <div class="domain-btn">SEARCH DOMAINS</div>
  </form>
  <div class="slider-dots" style="left:576px;top:486px"><i></i><i></i><i class="on"></i><i></i></div>
</section>

<section class="services">
  <div class="service" style="left:82px">
    <div class="service-icon"><svg width="60" height="60" viewBox="0 0 60 60"><circle cx="34" cy="26" r="20" fill="#fff"/><rect x="8" y="28" width="20" height="26" fill="#fff" stroke="#1fb5b8" stroke-width="2"/><path d="M12 34h12M12 40h12M12 46h12" stroke="#1fb5b8" stroke-width="2"/></svg></div>
    <h3>Website Hosting</h3>
    <p>Lorem ipsum dolor sit amet, loco<br>nsecte turelit dolo roin ultricies ve<br>stibulum velit. bibuco nd im.</p>
  </div>
  <div class="service" style="left:355px">
    <div class="service-icon"><svg width="60" height="60" viewBox="0 0 60 60"><rect x="26" y="10" width="22" height="40" fill="#fff"/><rect x="12" y="22" width="16" height="28" fill="#fff" stroke="#1fb5b8" stroke-width="2"/><path d="M15 30h10M15 37h10M15 44h10M30 18h14" stroke="#1fb5b8" stroke-width="2"/></svg></div>
    <h3>Dedicated Server</h3>
    <p>Lorem ipsum dolor sit amet, loco<br>nsecte turelit dolo roin ultricies ve<br>stibulum velit. bibuco nd im.</p>
  </div>
  <div class="service" style="left:615px">
    <div class="service-icon"><svg width="60" height="60" viewBox="0 0 60 60"><circle cx="30" cy="30" r="21" fill="none" stroke="#fff" stroke-width="4"/><ellipse cx="30" cy="30" rx="9" ry="21" fill="none" stroke="#fff" stroke-width="3"/><path d="M9 30h42M13 19h34M13 41h34" stroke="#fff" stroke-width="3"/></svg></div>
    <h3>Domain Name</h3>
    <p>Lorem ipsum dolor sit amet, loco<br>nsecte turelit dolo roin ultricies ve<br>stibulum velit. bibuco nd im.</p>
  </div>
  <div class="service" style="left:875px">
    <div class="service-icon"><svg width="60" height="60" viewBox="0 0 60 60"><rect x="10" y="16" width="40" height="30" fill="#fff"/><path d="M10 16l20 17 20-17" fill="none" stroke="#1fb5b8" stroke-width="2.5"/></svg></div>
    <h3>Email Solutions</h3>
    <p>Lorem ipsum dolor sit amet, loco<br>nsecte turelit dolo roin ultricies ve<br>stibulum velit. bibuco nd im.</p>
  </div>
</section>

<div class="divider"></div>

<h2 class="section-title" style="left:99px;top:1011px">Video Case <span>Studies</span></h2>
<article class="case" style="left:99px">
  <div class="case-thumb" role="img" aria-label="Video still of a woman working at a server cabinet"><svg width="40" height="30" viewBox="0 0 40 30"><rect width="40" height="30" rx="4" fill="#111"/><path d="M15 8l12 7-12 7z" fill="#fff"/></svg></div>
  <h4>Video Case Studies</h4>
  <p>Lorem ipsum dolor sit amet, consecte turel<br>it dolo. Proin ultricies vestibulum velit. bibum<br>co nd imentu mmetusip dolore ipsum.</p>
  <div class="rating">Rating: <span class="stars">★★★★★</span></div>
</article>
<article class="case" style="left:441px">
  <div class="case-thumb" role="img" aria-label="Video still of server racks in a bright data centre" style="background:linear-gradient(135deg,#9aa3ab,#3b4047)"><svg width="40" height="30" viewBox="0 0 40 30"><rect width="40" height="30" rx="4" fill="#111"/><path d="M15 8l12 7-12 7z" fill="#fff"/></svg></div>
  <h4>Video Case Studies</h4>
  <p>Lorem ipsum dolor sit amet, consecte turel<br>it dolo. Proin ultricies vestibulum velit. bibum<br>co nd imentu mmetusip dolore ipsum.</p>
  <div class="rating">Rating: <span class="stars">★★★★★</span></div>
</article>
<article class="case" style="left:784px">
  <div class="case-thumb" role="img" aria-label="Video still of a hand holding a glowing chart in front of servers" style="background:linear-gradient(135deg,#4b6a7c,#161b21)"><svg width="40" height="30" viewBox="0 0 40 30"><rect width="40" height="30" rx="4" fill="#111"/><path d="M15 8l12 7-12 7z" fill="#fff"/></svg></div>
  <h4>Video Case Studies</h4>
  <p>Lorem ipsum dolor sit amet, consecte turel<br>it dolo. Proin ultricies vestibulum velit. bibum<br>co nd imentu mmetusip dolore ipsum.</p>
  <div class="rating">Rating: <span class="stars">★★★★★</span></div>
</article>

<section class="testimonials">
  <h2 class="section-title" style="left:102px;top:33px">Client <span>Testimonials</span></h2>
  <div class="quote-card" style="left:97px">
    <p>“ This is Layerwise's version of Lorem Ipsum. Proin gravida nibh vel velit auctor aliquet. Aenean sollici-tudin, lorem quis bibendum auctor, nisi elit conse-quat ipsum, nec sagittis sem nibh id elit. ”</p>
    <div class="quote-by">-Elsie <span>★★★★</span></div>
  </div>
  <div class="avatar" role="img" aria-label="Client portrait" style="left:314px;top:219px"></div>
  <div class="quote-card" style="left:440px">
    <p>“ This is Layerwise's version of Lorem Ipsum. Proin gravida nibh vel velit auctor aliquet. Aenean sollici-tudin, lorem quis bibendum auctor, nisi elit conse-quat ipsum, nec sagittis sem nibh id elit. ”</p>
    <div class="quote-by">-Elsie <span>★★★★</span></div>
  </div>
  <div class="avatar" role="img" aria-label="Client portrait" style="left:657px;top:219px"></div>
  <div class="quote-card" style="left:783px">
    <p>“ This is Layerwise's version of Lorem Ipsum. Proin gravida nibh vel velit auctor aliquet. Aenean sollici-tudin, lorem quis bibendum auctor, nisi elit conse-quat ipsum, nec sagittis sem nibh id elit. ”</p>
    <div class="quote-by">-Elsie <span>★★★★</span></div>
  </div>
  <div class="avatar" role="img" aria-label="Client portrait" style="left:1000px;top:219px;background:linear-gradient(160deg,#d9d4cf,#8f96a0)"></div>
</section>

<h2 class="section-title" style="left:0;width:1200px;text-align:center;top:1866px">Murmel <span>Feeds</span></h2>
<div class="feed-name"><b>Mara Pell</b> @quaynotes</div>
<p class="feed-text">Nulla tincidunt elit a mauris pulvinar molestie aecenas vel nunc vitae dui mollis auctor Proin in dolor eu urna sagittis fring illa. Nulla suscipit laculla tincid <a>@unt elit a mauris pulvinar molesti</a> cenas vel nunc vitae dui mollis auctor. Proin in dolor eu urna sagittis fring illaulla suscipit lacus arcu, ac rutrum tellus feugiat sit</p>
<div class="feed-actions"><span>↩ Reply</span><span>⇄ Repost</span><span>★ Favorite</span><span>••• More</span></div>
<div class="slider-dots" style="left:576px;top:2092px"><i style="background:#d8d8d8"></i><i style="background:#d8d8d8"></i><i class="on"></i><i style="background:#d8d8d8"></i></div>

<footer class="site-footer">
  <div class="foot-col" style="left:99px"><h5>Our Company</h5><ul><li>About Us</li><li>Contact Us</li><li>Work For Us</li><li>Become An Affiliate</li><li>Read Our Blog</li><li>Site Map</li></ul></div>
  <div class="foot-col" style="left:297px"><h5>Useful Links</h5><ul><li>Online Control Panel</li><li>WebMail Login</li><li>Network Status</li><li>Terms &amp; Conditions</li><li>Sell Your Portfolio</li></ul></div>
  <div class="foot-col" style="left:486px"><h5>Create Account</h5><p>Set up a tallyfold.co.uk account and get access to a hub of resources and special offers.</p></div>
  <div class="foot-col" style="left:695px"><h5>Help &amp; Support</h5><ul><li>contact us</li><li>service status</li><li>CHI control panel login</li><li>knowledge base</li><li>Sitemap</li><li>support center</li></ul></div>
  <div class="foot-col" style="left:917px"><h5>Call us on:</h5>
    <div class="foot-phone">0345 555 0192</div>
    <div class="foot-phone-small">+44 (0)345 555 0192</div>
    <div class="socials"><i aria-label="Chatterleaf"></i><i aria-label="Murmel"></i><i aria-label="Zorbix+"></i><i aria-label="workLoop"></i><i aria-label="Vidplume"></i></div>
  </div>
  <div class="tagline">Real people with the right solutions to help you succeed online</div>
</footer>
<div class="copy-bar">Copyright ©2015 quayserverlantern.com. All rights reserved.</div>

</body>
</html>
```